fun theme dental practice website!

This client LOVES their superhero theme! They are an established pediatric dental practice with multiple locations. They have recently expanded to see adults and do orthodontics. They would like to have a new website design for the adult part of their practice. It should be similar in theme (superhero) but more adult (no sugarbugs!) . Navigation: about, meet the team, treatments, orthodontics, contact
add appointment request feature

Target Market(s)

adults

Industry/Entity Type

Dental

Number of Pages Required

2 page

Requirements
Must have
• home page design and interior page design
• fun and in theme but not too babyish (should it still look like a comic book?)
• appointment request feature
• visual pow
• colors consistent with logo (see attached)
• use the tooth social media icons

```html
<!DOCTYPE html>
<html lang="en">
<head>
<meta charset="utf-8">
<title>Valor Dental &amp; Orthodontics</title>
<link rel="stylesheet" href="https://fonts.googleapis.com/css2?family=Ubuntu:wght@400;500;700&family=Lato:wght@400;700&display=swap">
<style>
:root{
  --navy:#0f1450;
  --navy-deep:#1a1d5c;
  --green:#8dc63f;
  --red:#e8262d;
  --yellow:#fff000;
  --dark:#2b2b2d;
  --ink:#222;
  --white:#fff;
  --field:#fff;
  --paper:#f1f1f1;
}
*{box-sizing:border-box;margin:0;padding:0}
html,body{width:1200px;height:2403px;overflow:hidden}
body{position:relative;font-family:"Lato",sans-serif;color:var(--ink);background:var(--white)}
.abs{position:absolute}
.btn{position:absolute;display:flex;align-items:center;justify-content:center;background:var(--yellow);color:#111;font:500 15px "Ubuntu",sans-serif}

/* top bar */
.topbar{left:0;top:0;width:1200px;height:40px;background:var(--navy);color:#fff;font-size:13px}
.topbar .contact-item{position:absolute;top:12px;display:flex;align-items:center;gap:8px}
.tooth-links{position:absolute;right:60px;top:6px;display:flex;gap:14px}
.tooth-links span{width:30px;height:30px;background:var(--yellow);border-radius:8px 8px 12px 12px}

/* header */
.header{left:0;top:40px;width:1200px;height:103px;background:var(--green)}
.header .brand-panel{position:absolute;left:0;top:0}
.brand{position:absolute;left:58px;top:34px;font:700 22px "Ubuntu",sans-serif;color:var(--navy);line-height:1.1;width:220px}
.nav{position:absolute;left:367px;top:42px;display:flex;gap:0;font:400 15px "Ubuntu",sans-serif;color:#fff;text-transform:uppercase}
.nav a{position:absolute;white-space:nowrap;color:#fff;text-decoration:none}
.nav a.active{color:var(--red)}

/* hero */
.hero{left:0;top:143px;width:1200px;height:411px;background:linear-gradient(100deg,#6d6d6d 0%,#9a9a9a 40%,#d8d8d8 70%,#bdbdbd 100%)}
.hero-title{left:72px;top:248px;font:500 48px "Ubuntu",sans-serif;color:#fff}
.hero-text{left:72px;top:330px;width:480px;font-size:15px;line-height:1.5;color:#fff}
.slider-arrow{top:324px;width:36px;height:36px;background:#2a2a2a;display:flex;align-items:center;justify-content:center}

/* feature boxes */
.feature{top:554px;width:359px;height:321px;color:#fff;text-align:center}
.feature h3{position:absolute;left:0;right:0;top:140px;font:400 29px "Ubuntu",sans-serif}
.feature p{position:absolute;left:55px;right:55px;top:205px;font-size:13px;line-height:1.3}
.feature svg{position:absolute;left:50%;top:68px;transform:translateX(-50%)}
.f-doctors{left:61px;background:linear-gradient(135deg,#9ccf55,#8dc63f)}
.f-appoint{left:420px;background:linear-gradient(135deg,#ec3a3f,#e8262d)}
.f-ortho{left:780px;width:359px;background:var(--navy-deep)}

/* welcome */
.welcome-title{left:0;width:1200px;top:916px;text-align:center;font:400 32px "Ubuntu",sans-serif;color:var(--green)}
.welcome-title span{color:var(--red)}
.welcome-text{left:216px;top:1025px;width:798px;text-align:center;font-size:13px;line-height:1.55;color:#222}
.mascot-left{left:13px;top:945px;width:195px;height:196px;border-radius:40% 40% 30% 30%;background:linear-gradient(180deg,#eaf3fb,#c9def0)}
.mascot-right{left:1020px;top:910px;width:133px;height:259px;border-radius:40px 40px 10px 10px;background:linear-gradient(180deg,#e2c3a0,#2e3f62)}

/* reviews */
.reviews{left:0;top:1214px;width:1200px;height:452px;background:linear-gradient(180deg,#3a3a3c,#262628)}
.reviews-title{left:0;width:1200px;top:1262px;text-align:center;font:400 32px "Ubuntu",sans-serif;color:var(--green)}
.reviews-title span{color:var(--red)}
.review{top:1386px;width:516px;height:224px;border:1px solid #bdbdbd;color:#fff}
.review .quote{position:absolute;left:0;right:0;top:14px;text-align:center;font:700 56px "Ubuntu",sans-serif;line-height:1}
.review p{position:absolute;left:40px;right:40px;top:62px;text-align:center;font-size:14px;line-height:1.45}
.review .avatar{position:absolute;left:90px;top:128px;width:80px;height:80px;border-radius:50%;background:linear-gradient(180deg,#d9d9d9,#8e8e8e);border:3px solid #fff}
.review .name{position:absolute;left:185px;top:142px;font:700 14px "Lato",sans-serif}
.review .role{position:absolute;left:185px;top:164px;font-size:13px}

/* contact */
.contact{left:0;top:1666px;width:1200px;height:461px;background:var(--paper)}
.contact-title{left:59px;top:1718px;font:400 32px "Ubuntu",sans-serif;color:var(--green)}
.contact-title span{color:var(--red)}
.field{position:absolute;background:var(--field);color:#555;font-size:12px;padding:10px 10px}
.map{left:0;top:1666px}

/* footer */
.footer{left:0;top:2127px;width:1200px;height:225px;background:var(--green);color:#fff}
.footer h4{position:absolute;top:50px;font:700 18px "Ubuntu",sans-serif}
.footer .rule{position:absolute;top:86px;width:30px;height:2px;background:#fff}
.footer .lines{position:absolute;top:108px;font-size:15px;line-height:25px}
.footer .lines b{font-weight:700}
.footer .row{display:flex;align-items:center;gap:8px}
.bottombar{left:0;top:2352px;width:1200px;height:51px;background:var(--navy);color:#fff;font-size:13px}
.social{position:absolute;top:0;width:46px;height:51px;background:#1e3b9c;display:flex;align-items:center;justify-content:center}
.social span{width:14px;height:14px;background:#fff;border-radius:50%}
</style>
</head>
<body>

<!-- top bar -->
<div class="abs topbar">
  <div class="contact-item" style="left:63px">
    <svg width="14" height="14" viewBox="0 0 24 24"><path fill="#fff000" d="M6.6 10.8a15 15 0 0 0 6.6 6.6l2.2-2.2c.3-.3.7-.4 1-.2 1.1.4 2.3.6 3.6.6.6 0 1 .4 1 1V20c0 .6-.4 1-1 1A17 17 0 0 1 3 4c0-.6.4-1 1-1h3.5c.6 0 1 .4 1 1 0 1.2.2 2.4.6 3.6.1.3 0 .7-.2 1z"/></svg>
    (123) 456 - 7890
  </div>
  <div class="contact-item" style="left:205px">
    <svg width="16" height="12" viewBox="0 0 16 12"><rect width="16" height="12" rx="1" fill="#fff000"/><path d="M0 0l8 6 8-6" stroke="#0f1450" fill="none"/></svg>
    hello@valordentalortho.com
  </div>
  <div class="tooth-links"><span></span><span></span><span></span><span></span></div>
</div>

<!-- header -->
<div class="abs header">
  <svg class="brand-panel" width="340" height="103"><polygon points="0,0 282,0 336,103 0,103" fill="#fff"/></svg>
  <div class="brand">Valor Dental &amp; Orthodontics</div>
  <nav class="nav">
    <a class="active" style="left:0">Home</a>
    <a style="left:78px">About&nbsp; Us</a>
    <a style="left:189px">Meet the Team</a>
    <a style="left:335px">Treatments</a>
    <a style="left:463px">Contact Us</a>
  </nav>
  <div class="btn" style="left:955px;top:34px;width:184px;height:36px">Make An Appointment</div>
</div>

<!-- hero -->
<div class="abs hero" role="img" aria-label="Photo of a dentist treating a patient in the dental chair"></div>
<div class="abs hero-title">Amazing Treatment</div>
<div class="abs hero-text">Lorem ipsum dolor sit amet, consectetuer adipiscing elit, sed diam nonummy nibh euismod tincidunt ut laoreet</div>
<div class="btn" style="left:72px;top:399px;width:141px;height:35px">Contact Us</div>
<div class="abs slider-arrow" style="left:13px"><svg width="10" height="12"><path d="M8 1L2 6l6 5" stroke="#fff" stroke-width="2" fill="none"/></svg></div>
<div class="abs slider-arrow" style="left:1150px"><svg width="10" height="12"><path d="M2 1l6 5-6 5" stroke="#fff" stroke-width="2" fill="none"/></svg></div>

<!-- features -->
<div class="abs feature f-doctors">
  <svg width="56" height="60" viewBox="0 0 56 60"><circle cx="28" cy="16" r="12" fill="#fff"/><path d="M4 60c0-16 10-26 24-26s24 10 24 26z" fill="#fff"/><rect x="25" y="42" width="6" height="12" fill="#8dc63f"/><rect x="22" y="45" width="12" height="6" fill="#8dc63f"/></svg>
  <h3>Meet the Doctors</h3>
  <p>Lorem ipsum dolor sit amet, consectetur adipisicing elit. Rem adipisci veniam, hic, possimus officia.</p>
</div>
<div class="abs feature f-appoint">
  <svg width="56" height="58" viewBox="0 0 56 58"><rect x="3" y="8" width="50" height="48" rx="3" fill="none" stroke="#fff" stroke-width="4"/><rect x="3" y="8" width="50" height="10" fill="#fff"/><rect x="13" y="2" width="5" height="12" fill="#fff"/><rect x="38" y="2" width="5" height="12" fill="#fff"/><g fill="#fff"><rect x="11" y="24" width="7" height="6"/><rect x="21" y="24" width="7" height="6"/><rect x="31" y="24" width="7" height="6"/><rect x="41" y="24" width="5" height="6"/><rect x="11" y="34" width="7" height="6"/><rect x="21" y="34" width="7" height="6"/><rect x="31" y="34" width="7" height="6"/><rect x="41" y="34" width="5" height="6"/><rect x="11" y="44" width="7" height="6"/><rect x="21" y="44" width="7" height="6"/></g></svg>
  <h3>Make an Appointment</h3>
  <p>Lorem ipsum dolor sit amet, consectetur adipisicing elit. Rem adipisci veniam, hic, possimus officia.</p>
</div>
<div class="abs feature f-ortho">
  <svg width="44" height="60" viewBox="0 0 44 60"><path d="M22 6C14 0 2 2 2 16c0 10 4 16 6 28 2 12 8 14 10 4l4-12 4 12c2 10 8 8 10-4 2-12 6-18 6-28C42 2 30 0 22 6z" fill="#fff"/><rect x="4" y="20" width="36" height="5" fill="#1a1d5c"/><rect x="15" y="16" width="14" height="13" fill="#1a1d5c"/><rect x="18" y="19" width="8" height="7" fill="#fff"/></svg>
  <h3>Orthodontics</h3>
  <p>Lorem ipsum dolor sit amet, consectetur adipisicing elit. Rem adipisci veniam, hic, possimus officia.</p>
</div>

<!-- welcome -->
<div class="abs mascot-left" role="img" aria-label="Cartoon tooth character giving a thumbs up"></div>
<div class="abs mascot-right" role="img" aria-label="Cartoon man in a jacket giving a thumbs up"></div>
<div class="abs welcome-title">Welcome to <span>Valor Dental &amp; Orthodontics</span></div>
<svg class="abs" style="left:585px;top:966px" width="30" height="36" viewBox="0 0 44 60"><path d="M22 6C14 0 2 2 2 16c0 10 4 16 6 28 2 12 8 14 10 4l4-12 4 12c2 10 8 8 10-4 2-12 6-18 6-28C42 2 30 0 22 6z" fill="#1a1d5c"/></svg>
<div class="abs welcome-text">Lorem ipsum dolor sit amet, consectetuer adipiscing elit, sed diam nonummy nibh euismod tincidunt ut laoreet dolore magna aliquam erat volutpat. Ut wisi enim ad minim veniam, quis nostrud exerci tation ullamcorper suscipit lobortis nisl ut aliquip ex ea commodo consequat. Duis autem vel eum iriure dolor in hendrerit in vulputate velit esse molestie consequat, vel illum dolore eu feugiat nulla facilisis at vero eros et accumsan et iusto odio dignissim qui blandit praesent luptatum zzril delenit augue duis dolore te</div>
<div class="btn" style="left:529px;top:1136px;width:142px;height:35px">Read More</div>

<!-- reviews -->
<div class="abs reviews" role="img" aria-label="Dimmed photo of a dental visit behind the reviews"></div>
<div class="abs reviews-title">Customer <span>Reviews</span></div>
<svg class="abs" style="left:585px;top:1312px" width="30" height="36" viewBox="0 0 44 60"><path d="M22 6C14 0 2 2 2 16c0 10 4 16 6 28 2 12 8 14 10 4l4-12 4 12c2 10 8 8 10-4 2-12 6-18 6-28C42 2 30 0 22 6z" fill="#fff"/></svg>
<div class="abs review" style="left:59px">
  <div class="quote">&ldquo;</div>
  <p>Lorem ipsum dolor sit amet, consectetuer adipiscing elit. Aenean commodo ligula eget dolor. Aenean massa.</p>
  <div class="avatar" role="img" aria-label="Reviewer portrait"></div>
  <div class="name">Sam Porter</div>
  <div class="role">Lorem ipsum dolor sit</div>
</div>
<div class="abs review" style="left:623px">
  <div class="quote">&ldquo;</div>
  <p>Lorem ipsum dolor sit amet, consectetuer adipiscing elit. Aenean commodo ligula eget dolor. Aenean massa.</p>
  <div class="avatar" role="img" aria-label="Reviewer portrait"></div>
  <div class="name">Sam Porter</div>
  <div class="role">Lorem ipsum dolor sit</div>
</div>

<!-- contact -->
<div class="abs contact"></div>
<svg class="abs map" width="1200" height="461" role="img" aria-label="Map of the clinic locations">
  <defs><linearGradient id="mapTone" x1="0" y1="0" x2="1" y2="1"><stop offset="0" stop-color="#ece6d6"/><stop offset="1" stop-color="#dcd8c4"/></linearGradient></defs>
  <polygon points="606,0 1200,0 1200,461 610,461 670,240" fill="url(#mapTone)"/>
</svg>
<div class="abs contact-title">Send Us <span>Message</span></div>
<div class="field" style="left:61px;top:1778px;width:231px;height:37px">Name</div>
<div class="field" style="left:327px;top:1778px;width:232px;height:37px">Last name</div>
<div class="field" style="left:61px;top:1826px;width:231px;height:37px">Phone</div>
<div class="field" style="left:327px;top:1826px;width:232px;height:37px">E-mail</div>
<div class="field" style="left:61px;top:1876px;width:498px;height:149px">Message</div>
<div class="btn" style="left:415px;top:2046px;width:142px;height:40px">Submit</div>

<!-- footer -->
<div class="abs footer">
  <h4 style="left:59px">Come To Our Clinic</h4>
  <div class="rule" style="left:59px"></div>
  <div class="lines" style="left:59px"><b>Valor Dental &amp; Orthodontics</b><br>Donec porttitor entume suscipit..Nsequat<br>sem cursus - BT 58966</div>
  <h4 style="left:473px">Clinic Hour</h4>
  <div class="rule" style="left:473px"></div>
  <div class="lines" style="left:473px"><b>Monday to Friday: 8:00am - 17:00pm<br>Saturday: 9am - 14:00pm<br>Sunday: Closed</b></div>
  <h4 style="left:814px">Contact Us</h4>
  <div class="rule" style="left:814px"></div>
  <div class="lines" style="left:814px">
    <div class="row"><svg width="14" height="10"><rect width="14" height="10" fill="#fff"/><path d="M0 0l7 5 7-5" stroke="#8dc63f" fill="none"/></svg><b>hello@valordentalortho.com</b></div>
    <div class="row"><svg width="14" height="14" viewBox="0 0 24 24"><path fill="#fff" d="M6.6 10.8a15 15 0 0 0 6.6 6.6l2.2-2.2c.3-.3.7-.4 1-.2 1.1.4 2.3.6 3.6.6.6 0 1 .4 1 1V20c0 .6-.4 1-1 1A17 17 0 0 1 3 4c0-.6.4-1 1-1h3.5c.6 0 1 .4 1 1 0 1.2.2 2.4.6 3.6.1.3 0 .7-.2 1z"/></svg>(123) 456 - 7890</div>
    <div class="row"><svg width="14" height="13"><rect x="3" y="0" width="8" height="4" fill="#fff"/><rect x="0" y="4" width="14" height="6" fill="#fff"/><rect x="3" y="8" width="8" height="5" fill="#fff"/></svg>(123) 456 - 7890</div>
  </div>
</div>
<div class="abs bottombar">
  <div style="position:absolute;left:61px;top:17px">Copyright &copy; 2016 Valor Dental &amp; Orthodontics.&nbsp; All Rights Reserved.</div>
  <div class="social" style="left:952px"><span></span></div>
  <div class="social" style="left:999px"><span></span></div>
  <div class="social" style="left:1046px"><span></span></div>
  <div class="social" style="left:1093px"><span></span></div>
</div>

</body>
</html>
```